App Design for a petrol price in Nigeria

Through your already existing prototypes, we intend to design an app that would show petrol prices in Nigeria. The app would enable the user monitor the prices of petrol products in real time from nearby stations.

Industry/Entity Type

Gas And Oil

Requirements
Must have
• User community (sign up) and crowdsourced database integration

```html
<!DOCTYPE html>
<html lang="en">
<head>
<meta charset="utf-8">
<title>PumpWatch NG – App Screens</title>
<link href="https://fonts.googleapis.com/css2?family=Roboto:wght@400;500;700&display=swap" rel="stylesheet">
<style>
:root{
  --bg:#03bfad;
  --teal:#0cbfad;
  --teal-dark:#165d56;
  --white:#ffffff;
  --paper:#f2f2f2;
  --line:#e4e4e4;
  --ink:#2f2f2f;
  --muted:#9a9a9a;
  --map:#ececec;
  --yellow:#f7d51d;
}
*{box-sizing:border-box;margin:0;padding:0}
html,body{width:952px;height:1200px;overflow:hidden;background:var(--bg);font-family:'Roboto',sans-serif;color:var(--ink)}
.canvas{position:relative;width:952px;height:1200px;background:var(--bg)}
.screen{position:absolute;width:360px;height:740px;transform:scale(.674);transform-origin:0 0;overflow:hidden;border-radius:26px;background:var(--paper)}
.a{position:absolute;transform:translateY(-50%);white-space:nowrap}
.c{position:absolute;transform:translate(-50%,-50%);white-space:nowrap}
.box{position:absolute}
.header{position:absolute;left:0;top:0;width:360px;height:95px;background:var(--teal)}
.header-title{color:var(--white);font-weight:700;font-size:16px}
.burger{position:absolute;left:14px;width:24px;height:16px;transform:translateY(-50%)}
.burger span{display:block;height:2px;background:var(--white);margin-bottom:5px}
.avatar{position:absolute;border-radius:50%;background:radial-gradient(circle at 50% 40%,#8a5a3c,#3b2a22);border:2px solid var(--white)}
.navbar{position:absolute;left:0;top:675px;width:360px;height:65px;background:var(--white);border-top:1px solid var(--line)}
.nav-item{position:absolute;top:12px;transform:translateX(-50%);text-align:center;font-size:9px;color:#9a9a9a;letter-spacing:.3px}
.nav-item svg{display:block;margin:0 auto 6px;width:18px;height:18px}
.nav-item.active{color:var(--teal)}
.pill{position:absolute;border-radius:24px}
/* splash */
.splash{background:var(--teal)}
.brand-square{position:absolute;left:132px;top:283px;width:94px;height:105px;background:var(--white);border-radius:6px}
.brand-name{color:var(--white);font-size:30px;font-weight:500;letter-spacing:-.5px}
/* login */
.outline-btn{border:1.5px solid var(--teal);background:var(--white);font-size:14px;color:var(--ink)}
.field{background:var(--white);font-size:13px;color:#b8b8b8}
.primary-btn{background:var(--teal);color:var(--white);font-size:13px;font-weight:500}
/* stations */
.map{position:absolute;background:var(--map)}
.table-card{position:absolute;left:18px;top:340px;width:322px;height:322px;background:var(--white);border-radius:8px;box-shadow:0 4px 12px rgba(0,0,0,.08);overflow:hidden}
.table-head{position:absolute;left:0;top:0;width:322px;height:40px;background:var(--teal);color:var(--white);font-weight:700;font-size:12px}
.row-price{font-size:13px;color:#666}
.row-name{font-size:13px;color:var(--teal);font-weight:500}
.row-dist{font-size:13px;color:#555}
.dot{position:absolute;width:20px;height:20px;border-radius:50%;transform:translateY(-50%)}
.row-line{position:absolute;left:18px;width:262px;height:1px;background:#eee}
/* sheet */
.sheet{position:absolute;left:0;top:240px;width:360px;height:500px;background:var(--white);border-radius:60px 60px 0 0}
.sheet-title{font-size:20px;font-weight:500;color:var(--ink)}
.label{font-size:12px;color:#888}
.seg{position:absolute;left:42px;top:315px;width:276px;height:40px;background:#e8e8e8;border-radius:20px;font-size:13px;color:#333}
.bar{position:absolute;bottom:0;background:#e0e0e0}
.knob{position:absolute;width:14px;height:14px;border-radius:50%;background:var(--teal);transform:translate(-50%,-50%)}
/* profile */
.progress-node{position:absolute;width:22px;height:22px;border-radius:50%;transform:translate(-50%,-50%);background:var(--white);border:2px solid #ccc;font-size:10px;font-weight:700;color:var(--teal);text-align:center;line-height:18px}
.progress-node.done{border-color:var(--teal)}
/* notifications */
.toggle{position:absolute;left:272px;width:44px;height:22px;border-radius:11px;background:var(--teal);transform:translateY(-50%)}
.toggle::after{content:"";position:absolute;right:3px;top:3px;width:16px;height:16px;border-radius:50%;background:var(--white)}
.setting{font-size:14px;color:var(--ink)}
</style>
</head>
<body>
<div class="canvas">

<!-- Splash -->
<section class="screen splash" style="left:59px;top:53px">
  <div class="brand-square"></div>
  <div class="c brand-name" style="left:180px;top:433px">PumpWatch NG</div>
</section>

<!-- Sign in -->
<section class="screen login" style="left:353px;top:53px">
  <div class="brand-square" style="top:104px;border-radius:8px;box-shadow:0 2px 8px rgba(0,0,0,.05)"></div>
  <div class="pill outline-btn" style="left:52px;top:269px;width:257px;height:46px"><span class="c" style="left:50%;top:50%">Friendly</span></div>
  <div class="pill outline-btn" style="left:52px;top:330px;width:257px;height:46px"><span class="c" style="left:50%;top:50%">Globe ID</span></div>
  <div class="c" style="left:180px;top:398px;font-size:13px">OR</div>
  <div class="pill field" style="left:52px;top:425px;width:257px;height:47px">
    <span class="a" style="left:32px;top:50%">Email</span>
    <svg class="a" style="left:206px;top:50%" width="18" height="13" viewBox="0 0 18 13"><rect width="18" height="13" rx="1" fill="#c8c8c8"/><path d="M1 1l8 6 8-6" stroke="#fff" stroke-width="1.5" fill="none"/></svg>
  </div>
  <div class="pill field" style="left:52px;top:486px;width:257px;height:47px">
    <span class="a" style="left:32px;top:50%">Password</span>
    <svg class="a" style="left:210px;top:50%" width="12" height="14" viewBox="0 0 12 14"><rect y="6" width="12" height="8" rx="1" fill="#c8c8c8"/><path d="M3 6V4a3 3 0 0 1 6 0v2" stroke="#c8c8c8" stroke-width="1.6" fill="none"/></svg>
  </div>
  <div class="pill primary-btn" style="left:52px;top:552px;width:257px;height:47px"><span class="c" style="left:50%;top:50%">SIGN IN</span></div>
  <div class="c" style="left:180px;top:620px;font-size:13px;color:var(--teal);font-weight:500">Forgot password?</div>
  <div class="c" style="left:180px;top:678px;font-size:13px">Don't have account? <b style="color:var(--teal);font-size:15px;font-weight:500">Sign Up</b></div>
</section>

<!-- Fuel stations -->
<section class="screen stations" style="left:647px;top:53px;background:var(--white)">
  <div class="map" role="img" aria-label="Street map of nearby area" style="left:0;top:95px;width:360px;height:580px"></div>
  <div class="box" style="left:195px;top:129px;width:120px;height:120px;border-radius:50%;background:rgba(247,213,29,.35)"></div>
  <svg class="box" style="left:237px;top:118px" width="40" height="56" viewBox="0 0 40 56"><path d="M20 2C10 2 2 10 2 20c0 13 18 32 18 32s18-19 18-32C38 10 30 2 20 2z" fill="var(--yellow)"/><circle cx="20" cy="20" r="8" fill="#fff"/></svg>
  <div class="box" style="left:250px;top:183px;width:14px;height:14px;border-radius:50%;background:#f29a3a"></div>
  <div class="header"></div>
  <div class="burger" style="top:69px"><span></span><span></span><span></span></div>
  <div class="c header-title" style="left:180px;top:69px">Fuel stations</div>
  <div class="avatar" role="img" aria-label="User profile photo" style="left:307px;top:50px;width:38px;height:38px"></div>

  <div class="pill" style="left:20px;top:276px;width:230px;height:44px;background:var(--white);box-shadow:0 2px 6px rgba(0,0,0,.06)">
    <svg class="a" style="left:14px;top:50%" width="22" height="22" viewBox="0 0 22 22"><circle cx="10" cy="10" r="8" stroke="#ccc" stroke-width="1.8" fill="none"/><path d="M16 16l5 5" stroke="#ccc" stroke-width="1.8"/></svg>
    <span class="a" style="left:43px;top:50%;font-size:13px;color:#bbb">Search station</span>
  </div>
  <div class="pill" style="left:264px;top:276px;width:76px;height:44px;background:var(--white);box-shadow:0 2px 6px rgba(0,0,0,.06)"><span class="c" style="left:50%;top:50%;font-size:14px;color:var(--teal);font-weight:500">Filter</span></div>

  <div class="table-card">
    <div class="table-head">
      <span class="a" style="left:18px;top:20px">Price</span>
      <span class="c" style="left:150px;top:20px">Filling Stations</span>
      <span class="c" style="left:257px;top:20px">Location</span>
    </div>
    <div class="box" style="left:298px;top:54px;width:6px;height:48px;border-radius:3px;background:var(--teal)"></div>
    <div class="box" style="left:298px;top:102px;width:6px;height:200px;border-radius:3px;background:#f0f0f0"></div>

    <span class="a row-price" style="left:18px;top:62px">₦225</span><span class="dot" style="left:117px;top:62px;background:#f26a2b"></span><span class="a row-name" style="left:149px;top:62px">Okpara</span><span class="a row-dist" style="left:244px;top:62px">800m</span>
    <div class="row-line" style="top:82px"></div>
    <span class="a row-price" style="left:18px;top:101px">₦225</span><span class="dot" style="left:117px;top:101px;background:#e5302c"></span><span class="a row-name" style="left:149px;top:101px">Tidewell</span><span class="a row-dist" style="left:244px;top:101px">850m</span>
    <div class="row-line" style="top:121px"></div>
    <span class="a row-price" style="left:18px;top:141px">₦225</span><span class="dot" style="left:117px;top:141px;background:#7bbf5a"></span><span class="a row-name" style="left:149px;top:141px">Corafuel</span><span class="a row-dist" style="left:240px;top:141px">2.6Km</span>
    <div class="row-line" style="top:160px"></div>
    <span class="a row-price" style="left:18px;top:180px">₦225</span><span class="dot" style="left:117px;top:180px;background:#2a5fb5"></span><span class="a row-name" style="left:149px;top:180px">Arkline</span><span class="a row-dist" style="left:244px;top:180px">900m</span>
    <div class="row-line" style="top:199px"></div>
    <span class="a row-price" style="left:18px;top:219px">₦225</span><span class="dot" style="left:117px;top:219px;background:#c0392b"></span><span class="a row-name" style="left:149px;top:219px">MBK</span><span class="a row-dist" style="left:246px;top:219px">12Km</span>
    <div class="row-line" style="top:239px"></div>
    <span class="a row-price" style="left:18px;top:259px">₦225</span><span class="dot" style="left:117px;top:259px;background:#f5a623"></span><span class="a row-name" style="left:149px;top:259px">Riverline</span><span class="a row-dist" style="left:240px;top:259px">2.5Km</span>
    <div class="row-line" style="top:278px"></div>
    <span class="a row-price" style="left:18px;top:298px">₦225</span><span class="dot" style="left:117px;top:298px;background:#2e8b3a"></span><span class="a row-name" style="left:149px;top:298px">Naija Pet</span><span class="a row-dist" style="left:244px;top:298px">200m</span>
  </div>

  <nav class="navbar">
    <div class="nav-item active" style="left:29px"><svg viewBox="0 0 18 18"><path d="M2 8l7-6 7 6v8H11v-5H7v5H2z" fill="none" stroke="currentColor" stroke-width="1.3"/></svg>HOME</div>
    <div class="nav-item" style="left:116px"><svg viewBox="0 0 18 18"><path d="M9 16S2 11 2 6.5A3.5 3.5 0 0 1 9 5a3.5 3.5 0 0 1 7 1.5C16 11 9 16 9 16z" fill="none" stroke="currentColor" stroke-width="1.3"/></svg>FAVOURITES</div>
    <div class="nav-item" style="left:225px"><svg viewBox="0 0 18 18"><path d="M4 13V8a5 5 0 0 1 10 0v5l1 1H3zM7.5 16h3" fill="none" stroke="currentColor" stroke-width="1.3"/></svg>NOTIFICATIONS</div>
    <div class="nav-item" style="left:326px"><svg viewBox="0 0 18 18"><circle cx="9" cy="5" r="3" fill="none" stroke="currentColor" stroke-width="1.3"/><path d="M3 16a6 6 0 0 1 12 0z" fill="none" stroke="currentColor" stroke-width="1.3"/></svg>PROFILE</div>
  </nav>
</section>

<!-- Sort & filter -->
<section class="screen filter" style="left:59px;top:625px;background:#6b6b6b">
  <div class="header" style="background:var(--teal-dark)"></div>
  <div class="box" style="left:212px;top:148px;width:86px;height:86px;border-radius:50%;background:rgba(200,180,40,.45)"></div>
  <div class="sheet"></div>
  <div class="a sheet-title" style="left:42px;top:289px">Sort Stations by</div>
  <div class="seg">
    <span class="c" style="left:53px;top:20px">PRICES <span style="color:var(--teal)">⇅</span></span>
    <div class="box" style="left:107px;top:0;width:2px;height:40px;background:var(--teal)"></div>
    <span class="c" style="left:149px;top:20px">A - Z <span style="color:var(--teal)">⇅</span></span>
    <div class="box" style="left:191px;top:0;width:2px;height:40px;background:var(--teal)"></div>
    <span class="c" style="left:233px;top:20px">KM <span style="color:var(--teal)">⇅</span></span>
  </div>
  <div class="a sheet-title" style="left:42px;top:410px">Filling Station Filter</div>
  <div class="a label" style="left:42px;top:450px">Price range</div>
  <div class="box" style="left:87px;top:454px;width:208px;height:55px">
    <div class="bar" style="left:0;width:17px;height:8px"></div>
    <div class="bar" style="left:19px;width:17px;height:20px"></div>
    <div class="bar" style="left:38px;width:17px;height:21px"></div>
    <div class="bar" style="left:57px;width:17px;height:33px"></div>
    <div class="bar" style="left:76px;width:17px;height:54px"></div>
    <div class="bar" style="left:95px;width:17px;height:40px"></div>
    <div class="bar" style="left:114px;width:17px;height:32px"></div>
    <div class="bar" style="left:133px;width:17px;height:28px"></div>
    <div class="bar" style="left:152px;width:17px;height:20px"></div>
    <div class="bar" style="left:171px;width:17px;height:10px"></div>
    <div class="bar" style="left:190px;width:17px;height:4px"></div>
  </div>
  <div class="box" style="left:42px;top:508px;width:276px;height:2px;background:#ddd"></div>
  <div class="box" style="left:106px;top:508px;width:162px;height:2px;background:var(--teal)"></div>
  <div class="knob" style="left:106px;top:509px"></div><div class="knob" style="left:268px;top:509px"></div>
  <div class="c label" style="left:104px;top:531px;color:#777">₦182</div>
  <div class="c label" style="left:266px;top:531px;color:#777">₦225</div>
  <div class="a label" style="left:42px;top:567px">Location</div>
  <div class="box" style="left:42px;top:592px;width:276px;height:2px;background:#ddd"></div>
  <div class="box" style="left:80px;top:592px;width:188px;height:2px;background:var(--teal)"></div>
  <div class="knob" style="left:80px;top:593px"></div><div class="knob" style="left:268px;top:593px"></div>
  <div class="c label" style="left:80px;top:615px;color:#777">50m</div>
  <div class="c label" style="left:268px;top:615px;color:#777">1Km</div>
  <div class="pill primary-btn" style="left:33px;top:649px;width:154px;height:42px;font-weight:700"><span class="c" style="left:50%;top:50%">APPLY FILTERS</span></div>
  <div class="pill" style="left:222px;top:649px;width:96px;height:42px;background:#eee;color:var(--teal);font-size:13px;font-weight:500"><span class="c" style="left:50%;top:50%">RESET</span></div>
</section>

<!-- Profile -->
<section class="screen profile" style="left:353px;top:625px">
  <div class="header" style="height:110px"></div>
  <div class="burger" style="top:69px"><span></span><span></span><span></span></div>
  <div class="map" role="img" aria-label="Faint street map behind profile" style="left:0;top:110px;width:360px;height:133px;border-radius:0 0 24px 24px;background:#f7f7f7;box-shadow:0 3px 6px rgba(0,0,0,.05)"></div>
  <div class="avatar" role="img" aria-label="Member profile photo" style="left:138px;top:73px;width:84px;height:84px;border-width:3px"></div>
  <div class="c" style="left:180px;top:179px;font-size:16px;font-weight:500">Kemi Adeyemi</div>
  <div class="c" style="left:180px;top:198px;font-size:10px;color:#999">Member since Sept. 2020</div>
  <div class="a" style="left:44px;top:278px;font-size:20px;font-weight:500">Contribute &amp; Save</div>
  <div class="a" style="left:44px;top:301px;font-size:10px;color:#888">Contribute, receive points and promos</div>
  <div class="box" style="left:57px;top:334px;width:248px;height:2px;background:#ddd"></div>
  <div class="box" style="left:57px;top:334px;width:124px;height:2px;background:var(--teal)"></div>
  <div class="progress-node done" style="left:57px;top:335px">₦</div>
  <div class="progress-node done" style="left:119px;top:335px">₦</div>
  <div class="progress-node done" style="left:181px;top:335px">₦</div>
  <div class="progress-node" style="left:243px;top:335px"></div>
  <div class="progress-node" style="left:305px;top:335px"></div>
  <div class="box" style="left:155px;top:358px;width:54px;height:31px;background:var(--teal);border-radius:2px;color:#fff;text-align:center;font-size:11px;font-weight:700;line-height:11px;padding-top:5px">40%<br><span style="font-size:8px">complete</span></div>
  <div class="a" style="left:44px;top:419px;font-size:13px;font-weight:700;color:var(--teal)">Ways to Save</div>
  <svg class="a" style="left:305px;top:419px" width="12" height="8" viewBox="0 0 12 8"><path d="M1 1l5 5 5-5" stroke="var(--teal)" stroke-width="1.6" fill="none"/></svg>
  <div class="box" style="left:44px;top:440px;width:273px;height:1px;background:var(--teal)"></div>
  <div class="box" style="left:44px;top:441px;width:273px;height:79px;background:var(--white)"></div>
  <div class="a" style="left:56px;top:472px;font-size:14px">Buy More, Pay less!</div>
  <div class="a" style="left:56px;top:489px;font-size:7.5px;color:#999">Every time you buy, you can earn badges and get special deals!</div>
  <div class="a" style="left:44px;top:542px;font-size:12px;color:#444">SETTINGS</div>
  <div class="a" style="left:44px;top:561px;font-size:12px;color:#444">Notifications</div>
  <div class="pill" style="left:44px;top:601px;width:273px;height:42px;background:#e2e2e2;color:var(--teal);font-size:14px;font-weight:500"><span class="c" style="left:50%;top:50%">SIGN OUT</span></div>
  <nav class="navbar">
    <div class="nav-item active" style="left:29px"><svg viewBox="0 0 18 18"><path d="M2 8l7-6 7 6v8H11v-5H7v5H2z" fill="none" stroke="currentColor" stroke-width="1.3"/></svg>HOME</div>
    <div class="nav-item" style="left:116px"><svg viewBox="0 0 18 18"><path d="M9 16S2 11 2 6.5A3.5 3.5 0 0 1 9 5a3.5 3.5 0 0 1 7 1.5C16 11 9 16 9 16z" fill="none" stroke="currentColor" stroke-width="1.3"/></svg>FAVOURITES</div>
    <div class="nav-item" style="left:225px"><svg viewBox="0 0 18 18"><path d="M4 13V8a5 5 0 0 1 10 0v5l1 1H3zM7.5 16h3" fill="none" stroke="currentColor" stroke-width="1.3"/></svg>NOTIFICATIONS</div>
    <div class="nav-item" style="left:326px"><svg viewBox="0 0 18 18"><circle cx="9" cy="5" r="3" fill="none" stroke="currentColor" stroke-width="1.3"/><path d="M3 16a6 6 0 0 1 12 0z" fill="none" stroke="currentColor" stroke-width="1.3"/></svg>PROFILE</div>
  </nav>
</section>

<!-- Notifications -->
<section class="screen notifications" style="left:647px;top:625px">
  <div class="box" style="left:0;top:95px;width:360px;height:352px;background:var(--white)"></div>
  <div class="header"></div>
  <div class="burger" style="top:69px"><span></span><span></span><span></span></div>
  <div class="c header-title" style="left:180px;top:69px">Notification</div>
  <div class="avatar" role="img" aria-label="User profile photo" style="left:307px;top:50px;width:38px;height:38px"></div>
  <div class="a" style="left:44px;top:145px;font-size:20px;color:var(--teal)">Push Notifications</div>
  <div class="a setting" style="left:44px;top:187px">Price Changes</div>
  <div class="toggle" style="top:187px"></div>
  <div class="box" style="left:44px;top:209px;width:272px;height:1px;background:#eee"></div>
  <div class="a setting" style="left:44px;top:230px">Petrol News &amp; Updates</div>
  <div class="toggle" style="top:230px"></div>
  <div class="box" style="left:44px;top:251px;width:272px;height:1px;background:#eee"></div>
  <div class="a setting" style="left:44px;top:266px">Promos &amp; Deals</div>
  <div class="a" style="left:44px;top:281px;font-size:7.5px;color:#999">Get access to deals and exclusive savings</div>
  <div class="toggle" style="top:273px"></div>
  <nav class="navbar">
    <div class="nav-item active" style="left:29px"><svg viewBox="0 0 18 18"><path d="M2 8l7-6 7 6v8H11v-5H7v5H2z" fill="none" stroke="currentColor" stroke-width="1.3"/></svg>HOME</div>
    <div class="nav-item" style="left:116px"><svg viewBox="0 0 18 18"><path d="M9 16S2 11 2 6.5A3.5 3.5 0 0 1 9 5a3.5 3.5 0 0 1 7 1.5C16 11 9 16 9 16z" fill="none" stroke="currentColor" stroke-width="1.3"/></svg>FAVOURITES</div>
    <div class="nav-item" style="left:225px"><svg viewBox="0 0 18 18"><path d="M4 13V8a5 5 0 0 1 10 0v5l1 1H3zM7.5 16h3" fill="none" stroke="currentColor" stroke-width="1.3"/></svg>NOTIFICATIONS</div>
    <div class="nav-item" style="left:326px"><svg viewBox="0 0 18 18"><circle cx="9" cy="5" r="3" fill="none" stroke="currentColor" stroke-width="1.3"/><path d="M3 16a6 6 0 0 1 12 0z" fill="none" stroke="currentColor" stroke-width="1.3"/></svg>PROFILE</div>
  </nav>
</section>

</div>
</body>
</html>
```